2021 Personalized Vision Poster

A beautiful, pleasing design for my 2021 vision poster. Looking probably for an infographic. Open to shortening the wording used if able. As you will notice, each color represents a different category. Let me know if you need more details. The title of each section are mostly listed, but starting with the upper left with “my primary question” going counter-clockwise: my primary question, away values and rules, life purpose, power values (red), toward values and rules, top 4 goals for 2021 (middle), and relationship vision (middle). Basically, I’m just looking for a nice font and different formatting for my words.

Requirements
Must have
• All of the sections with a majority of the words used.
Nice to have
• Infographic would be nice, if possible. More concerned with a beautiful layout of words already expressed.
Should not have
• A complete reworking of the words used.

```html
<!DOCTYPE html>
<html lang="en">
<head>
<meta charset="utf-8">
<title>Live Courageously – 2021 Vision Poster</title>
<link rel="stylesheet" href="https://fonts.googleapis.com/css2?family=Bebas+Neue&family=Lobster&display=swap">
<style>
  :root {
    --sky: #6ccbe0;
    --paper: #ffffff;
  }
  html, body {
    margin: 0;
    padding: 0;
    overflow: hidden;
    background: var(--paper);
  }
  .poster {
    position: relative;
    width: 848px;
    height: 1200px;
    overflow: hidden;
    background: var(--paper);
    font-family: "Bebas Neue", "Oswald", sans-serif;
    color: var(--paper);
    text-transform: uppercase;
  }
  .poster__bands {
    position: absolute;
    inset: 0;
  }
  .poster__bands polygon,
  .poster__bands rect { fill: var(--sky); }

  .t {
    position: absolute;
    margin: 0;
    padding: 0;
    line-height: 1;
    white-space: nowrap;
    transform-origin: left top;
    transform: rotate(-5deg);
  }
  .t li { list-style: none; }
  .t span { display: block; }
  .t--sky { color: var(--sky); }

  .title-script {
    position: absolute;
    margin: 0;
    font-family: "Lobster", cursive;
    color: var(--paper);
    text-transform: none;
    line-height: 1;
    white-space: nowrap;
    transform: rotate(-6deg);
    transform-origin: left top;
    -webkit-text-stroke: 3px var(--sky);
    paint-order: stroke fill;
    text-shadow: 4px 4px 0 var(--sky);
  }
  .title-script--small { left: 96px; top: 22px; font-size: 56px; }
  .title-script--big { left: 22px; top: 88px; font-size: 74px; }

  .year { left: 566px; top: 6px; font-size: 130px; letter-spacing: 2px; transform: none; }

  .goals-heading { left: 95px; top: 212px; font-size: 98px; letter-spacing: 3px; }
  .goals-list { left: 360px; top: 172px; font-size: 37px; line-height: 0.9; }
  .goals-list li:nth-child(3) { padding-left: 6px; }
  .goals-list li:nth-child(4) { padding-left: 12px; }

  .values-heading { left: 32px; top: 395px; font-size: 50px; }
  .rules-heading { left: 228px; top: 394px; font-size: 48px; }

  .item-list { font-size: 22px; line-height: 1.15; letter-spacing: 0.3px; }
  .toward-list { left: 388px; top: 368px; }
  .giving-list { left: 30px; top: 505px; }
  .avoid-list { left: 62px; top: 655px; line-height: 1.08; }

  .remember-heading { left: 422px; top: 526px; font-size: 36px; }
  .remember-list { left: 430px; top: 570px; font-size: 19.5px; line-height: 1.2; }

  .avoid-label { left: 12px; top: 748px; font-size: 34px; transform: rotate(-90deg); }

  .relationship { left: 452px; top: 690px; font-size: 54px; }

  .core-values { left: 100px; top: 770px; font-size: 100px; line-height: 0.85; }
  .core-values .respect { padding-left: 110px; font-size: 82px; }

  .power-values { left: 470px; top: 812px; font-size: 110px; line-height: 0.9; }
  .power-small { left: 510px; top: 1010px; font-size: 50px; }
  .power-small .presence { color: var(--sky); padding-left: 20px; padding-top: 5px; }

  .purpose-intro { left: 40px; top: 958px; font-size: 22px; }
  .purpose-line { left: 14px; top: 972px; font-size: 44px; }
  .purpose-fun { left: 14px; top: 1030px; font-size: 104px; }
  .purpose-adventure { left: 206px; top: 1000px; font-size: 42px; text-decoration: underline; text-decoration-thickness: 3px; text-underline-offset: 1px; }
  .purpose-play { left: 206px; top: 1046px; font-size: 46px; }
  .purpose-close { left: 46px; top: 1128px; font-size: 44px; }
</style>
</head>
<body>
<main class="poster">

  <svg class="poster__bands" width="848" height="1200" viewBox="0 0 848 1200" aria-hidden="true">
    <polygon points="0,195 330,166 330,335 0,364"/>
    <polygon points="340,162 848,118 848,290 340,334"/>
    <rect x="0" y="400" width="16" height="34"/>
    <polygon points="210,392 362,379 362,440 210,453"/>
    <polygon points="372,350 848,308 848,470 372,512"/>
    <polygon points="16,480 405,446 405,600 16,634"/>
    <polygon points="415,525 848,487 848,622 415,660"/>
    <polygon points="40,646 410,614 410,708 40,740"/>
    <rect x="8" y="655" width="28" height="100"/>
    <polygon points="0,776 460,736 460,915 0,955"/>
    <polygon points="0,1040 200,1022 200,1000 500,974 500,1090 0,1134"/>
    <polygon points="462,815 848,781 848,1081 462,1115"/>
  </svg>

  <p class="title-script title-script--small">Live</p>
  <p class="title-script title-script--big">Courageously!</p>
  <p class="t t--sky year">2021</p>

  <h2 class="t goals-heading">Goals</h2>
  <ol class="t goals-list">
    <li>1-Rental</li>
    <li>2-175lbs</li>
    <li>3-Team</li>
    <li>4-$250K</li>
  </ol>

  <h2 class="t t--sky values-heading">Values &amp;</h2>
  <h2 class="t rules-heading">Rules</h2>

  <ul class="t item-list toward-list">
    <li>- Practicing vulnerability,</li>
    <li>- Taking actions consistent with my identity,</li>
    <li>- Getting outdoors,</li>
    <li>- Going on a little or big adventure,</li>
    <li>- Moving my body!</li>
  </ul>

  <ul class="t item-list giving-list">
    <li>- Giving of myself and serve others,</li>
    <li>- Accepting love from God or others,</li>
    <li>- Doing something even when scary,</li>
    <li>- Choosing to put myself first,</li>
  </ul>

  <h2 class="t remember-heading">Remember</h2>
  <ul class="t item-list remember-list">
    <li>- I alone have the power to choose to be angry</li>
    <li>- God has made me a conqueror - I will not fail</li>
    <li>- God has given me all the inner peace I need</li>
  </ul>

  <h2 class="t avoid-label">Avoid</h2>
  <ul class="t item-list avoid-list">
    <li>- Unrighteous anger</li>
    <li>- Debilitating illusion of failure</li>
    <li>- Consistent debilitating anxiety</li>
  </ul>

  <h2 class="t t--sky relationship"><span>Relationship</span><span>Vision</span></h2>

  <p class="t core-values"><span>Joy Love</span><span class="respect">Respect</span></p>

  <p class="t power-values"><span>Power</span><span>Courage</span></p>
  <p class="t power-small">
    <span>Romantic</span>
    <span>Flirty</span>
    <span class="presence">Presence</span>
  </p>

  <p class="t t--sky purpose-intro">The purpose of my life is</p>
  <p class="t t--sky purpose-line">To be loving courageous</p>
  <p class="t purpose-fun">Fun!</p>
  <p class="t purpose-adventure">I seek adventure</p>
  <p class="t purpose-play">Laugh and play</p>
  <p class="t t--sky purpose-close">And live in God's identity</p>

</main>
</body>
</html>
```